Book Cover "Venice"

Creation of a cover (14 x 20.5 cm + bleed area) for a book:
Image: “BrumeVerte” (Tiff joined)
AUTHOR: Corinne Valmer
TITLE: The murmurs of Lorient
PUBLISHER: Editions Pluvane (AT THE BOTTOM OF THE COVER)

Target Market(s)

Readers of romantic novels

Industry/Entity Type

Book

```html
<!DOCTYPE html>
<html lang="en">
<head>
<meta charset="utf-8">
<title>The murmurs of Lorient — Corinne Valmer</title>
<link href="https://fonts.googleapis.com/css2?family=Great+Vibes&family=Marcellus&display=swap" rel="stylesheet">
<style>
  :root {
    --backdrop: #86a67c;
    --sky-deep: #3a0a0c;
    --sky-crimson: #b3151a;
    --sky-red: #d8241c;
    --sky-orange: #ec4a1c;
    --dusk: #1a0608;
    --ink-light: #ffffff;
    --publisher-red: #c8321f;
    --silver-light: #f4f4f4;
    --silver-mid: #c9c9c9;
    --silver-dark: #8f8f8f;
  }
  * { margin: 0; padding: 0; box-sizing: border-box; }
  html, body {
    width: 1200px;
    height: 1200px;
    overflow: hidden;
    background: var(--backdrop);
  }
  .canvas {
    position: relative;
    width: 1200px;
    height: 1200px;
    background: var(--backdrop);
  }
  .book-cover {
    position: absolute;
    left: 232px;
    top: 40px;
    width: 736px;
    height: 1120px;
    overflow: hidden;
  }
  .cover-photo {
    position: absolute;
    inset: 0;
    background:
      linear-gradient(180deg, rgba(0,0,0,0) 70%, var(--dusk) 98%),
      radial-gradient(ellipse 90% 45% at 60% 62%, var(--sky-orange) 0%, rgba(236,74,28,0) 70%),
      linear-gradient(180deg, var(--sky-deep) 0%, var(--sky-crimson) 22%, var(--sky-red) 50%, var(--sky-orange) 70%, var(--sky-crimson) 85%);
  }
  .title-block {
    position: absolute;
    inset: 0;
    font-weight: 400;
    color: var(--ink-light);
  }
  .title-initial {
    position: absolute;
    left: 40px;
    top: 246px;
    font-family: "Great Vibes", cursive;
    font-size: 220px;
    line-height: 1;
  }
  .title-article,
  .title-line,
  .title-word {
    position: absolute;
    right: 136px;
    font-family: "Marcellus", serif;
    line-height: 1;
    letter-spacing: 1px;
    white-space: nowrap;
    text-align: right;
  }
  .title-article {
    top: 272px;
    font-size: 38px;
  }
  .title-line {
    top: 326px;
    font-size: 38px;
  }
  .title-word {
    top: 384px;
    font-size: 90px;
  }
  .author {
    position: absolute;
    left: 158px;
    top: 503px;
    width: 444px;
    border-top: 3px solid var(--ink-light);
    border-bottom: 3px solid var(--ink-light);
    padding: 13px 0 11px;
    text-align: center;
    font-family: "Marcellus", serif;
    font-size: 46px;
    line-height: 1;
    color: var(--ink-light);
    letter-spacing: 1px;
    white-space: nowrap;
  }
  .publisher-band {
    position: absolute;
    left: 0;
    top: 1004px;
    width: 100%;
    height: 68px;
    background: linear-gradient(90deg, var(--silver-dark) 0%, var(--silver-light) 22%, var(--silver-mid) 55%, var(--silver-light) 80%, var(--silver-dark) 100%);
    display: flex;
    align-items: center;
    justify-content: center;
  }
  .publisher-name {
    font-family: "Marcellus", serif;
    font-size: 38px;
    line-height: 1;
    color: var(--publisher-red);
    letter-spacing: 1px;
    white-space: nowrap;
  }
</style>
</head>
<body>
  <main class="canvas">
    <article class="book-cover">
      <div class="cover-photo" role="img" aria-label="Photograph BrumeVerte: blazing red sunset sky over the domes and lamp posts of Lorient in silhouette"></div>
      <h1 class="title-block" aria-label="The murmurs of Lorient">
        <span class="title-initial">L</span>
        <span class="title-article">THE</span>
        <span class="title-line">MURMURS OF</span>
        <span class="title-word">ORIENT</span>
      </h1>
      <p class="author">CORINNE VALMER</p>
      <div class="publisher-band">
        <span class="publisher-name">EDITIONS PLUVANE</span>
      </div>
    </article>
  </main>
</body>
</html>
```